Business Card Design Project

Business and Appointment Card for Medical Practice. On back of card we would like to have: blank line for patient name, Mon-Fri each with a check box next to the day, blank line for appointment date, blank line for appointment time, with option to circle am or pm.

Target Market(s)

Professional Business Associates, as well as function as patient appointment cards (on back side of card)

Industry/Entity Type

Business

Colors

```html
<!DOCTYPE html>
<html lang="en">
<head>
<meta charset="utf-8">
<title>Maple Grove Medical Associates – Business &amp; Appointment Card</title>
<link href="https://fonts.googleapis.com/css2?family=Cinzel:wght@500&family=Open+Sans:wght@400&display=swap" rel="stylesheet">
<style>
  :root {
    --backdrop: #131311;
    --card: #fdfdfd;
    --ink: #1b1b1b;
    --crimson: #9a2329;
    --forest: #1f6a3a;
    --box: #d4d4d4;
    --coat-light: #f4f4f4;
    --coat-mid: #e2e2e2;
  }
  * { box-sizing: border-box; margin: 0; padding: 0; }
  html, body { width: 1188px; height: 1200px; overflow: hidden; }
  body {
    background: var(--backdrop);
    position: relative;
    font-family: "Open Sans", Arial, sans-serif;
  }
  .card {
    position: absolute;
    top: 170px;
    width: 470px;
    height: 860px;
    background: var(--card);
    overflow: hidden;
  }
  /* Back: appointment side */
  .card--back { left: 60px; }
  .coat-illustration {
    position: absolute;
    left: 0; top: 0;
    width: 470px; height: 470px;
    background: radial-gradient(ellipse at 50% 40%, var(--coat-light), var(--coat-mid));
  }
  .patient-line {
    position: absolute;
    left: 40px; right: 40px; top: 520px;
    border-top: 2px solid var(--ink);
  }
  .appointment-label {
    position: absolute;
    left: 0; right: 0; top: 530px;
    text-align: center;
    font-size: 17px;
    color: var(--ink);
    letter-spacing: 0.3px;
  }
  .weekdays {
    position: absolute;
    left: 30px; right: 30px; top: 600px;
    display: flex;
    justify-content: space-between;
  }
  .weekday {
    display: flex;
    flex-direction: column;
    align-items: center;
    gap: 8px;
    width: 70px;
  }
  .weekday__box {
    width: 22px; height: 22px;
    border: 1px solid #999;
    background: var(--box);
  }
  .weekday__name {
    color: var(--crimson);
    font-size: 17px;
  }
  .schedule {
    position: absolute;
    left: 30px; right: 30px; top: 690px;
    display: flex;
    align-items: flex-start;
    gap: 14px;
  }
  .schedule__field {
    flex: 1;
    border-top: 2px solid var(--ink);
    margin-top: 28px;
    text-align: center;
    font-size: 17px;
    color: var(--ink);
    padding-top: 4px;
  }
  .schedule__at { font-size: 22px; margin-top: 10px; color: var(--ink); }
  .schedule__meridiem { font-size: 17px; color: var(--ink); margin-top: 14px; }

  /* Front: identity side */
  .card--front { left: 658px; }
  .front-frame {
    position: absolute;
    inset: 16px;
    border: 3px solid var(--forest);
  }
  .front-layout {
    position: absolute;
    left: 50%; top: 50%;
    width: 828px; height: 438px;
    transform: translate(-50%, -50%) rotate(90deg);
    display: flex;
    align-items: center;
    justify-content: center;
    gap: 40px;
  }
  .practice-name {
    font-family: "Cinzel", Georgia, serif;
    font-weight: 500;
    color: var(--forest);
    line-height: 1.05;
  }
  .practice-name__main { display: block; font-size: 66px; letter-spacing: 1px; }
  .practice-name__sub { display: block; font-size: 37px; letter-spacing: 2px; }
  .practice-mark {
    width: 150px; height: 150px;
    border-radius: 50%;
    border: 3px solid var(--forest);
    flex: none;
  }
</style>
</head>
<body>
  <section class="card card--back" aria-label="Appointment side">
    <div class="coat-illustration" role="img" aria-label="Illustration of a white doctor's coat with red tie and stethoscope"></div>
    <div class="patient-line"></div>
    <p class="appointment-label">HAS AN APPOINTMENT ON</p>
    <div class="weekdays">
      <div class="weekday"><span class="weekday__box"></span><span class="weekday__name">MON</span></div>
      <div class="weekday"><span class="weekday__box"></span><span class="weekday__name">TUE</span></div>
      <div class="weekday"><span class="weekday__box"></span><span class="weekday__name">WED</span></div>
      <div class="weekday"><span class="weekday__box"></span><span class="weekday__name">THUR</span></div>
      <div class="weekday"><span class="weekday__box"></span><span class="weekday__name">FRI</span></div>
    </div>
    <div class="schedule">
      <div class="schedule__field">DATE</div>
      <span class="schedule__at">@</span>
      <div class="schedule__field">TIME</div>
      <span class="schedule__meridiem">AM / PM</span>
    </div>
  </section>

  <section class="card card--front" aria-label="Practice side">
    <div class="front-frame"></div>
    <div class="front-layout">
      <h1 class="practice-name">
        <span class="practice-name__main">MAPLE GROVE</span>
        <span class="practice-name__sub">MEDICAL ASSOCIATES</span>
      </h1>
      <span class="practice-mark" aria-hidden="true"></span>
    </div>
  </section>
</body>
</html>
```